Showroom Quote Web Application - Prism Layout wanted

This web app is an internal application that will be used by one of our customers to build quotes and produce orders of retail items with their customers

the overall design should use the colour pallet provided and have a clean and simple interface

we'd like to go with a prism layout type of look

attached mockups are just a rough stab at some layouts to give you an example, please feel free to reach out with any questions.

Please don't get hung up on the specific pages, they were intended to provide context, we are looking for a high level design using the provided colour schemes and fonts, additional work may follow for the selected designer when it comes to specific pages or work flows.

Sorry for the short timeline, we have a tight deadline on this one.

Target Market(s)

internal application for customer

Industry/Entity Type

Retail

Other font styles liked:
• see attached doc for fonts

Requirements
Must have
• simple and clean interface
• intuitive design
Nice to have
• see attached documents for logo colour schemes and fonts
• these must be incorporated into the design

```html
<!DOCTYPE html>
<html lang="en">
<head>
<meta charset="utf-8">
<title>Showroom Quote System – Prism Layout</title>
<link href="https://fonts.googleapis.com/css2?family=Roboto:wght@400;500;700&display=swap" rel="stylesheet">
<style>
:root{
  --navy:#002a6b;
  --navy-field:#3d5a8b;
  --gold:#b8954a;
  --page:#f5f5f5;
  --white:#ffffff;
  --ink:#212121;
  --ink-soft:#616161;
  --line:#e0e0e0;
  --stripe:#f7f7f7;
  --scrim:rgba(0,40,110,0.86);
}
*{box-sizing:border-box;margin:0;padding:0}
html,body{width:1200px;height:1200px;overflow:hidden;background:var(--page);font-family:'Roboto',sans-serif;color:var(--ink)}
.screen{position:absolute;left:157px;width:886px;height:554px;background:var(--page);overflow:hidden;box-shadow:0 1px 4px rgba(0,0,0,.12)}
.screen--list{top:31px}
.screen--quote{top:610px}
.appbar{position:absolute;left:0;top:0;width:100%;height:38px;background:var(--white);display:flex;align-items:center;padding:0 18px;z-index:2}
.menu-icon{width:13px;height:10px;margin-right:14px}
.brand{font-weight:700;font-size:12.5px;letter-spacing:.3px;color:#555}
.greeting{margin-left:auto;font-size:8px;color:#888;margin-right:20px}
.avatar{width:22px;height:22px;border-radius:50%;background:linear-gradient(160deg,#c8d6e6,#4a6fa0 55%,#1d3557)}
.more{margin-left:8px;width:3px;height:11px}
.band{position:absolute;left:0;top:38px;width:100%;background:var(--navy)}
.screen--list .band{height:188px}
.screen--quote .band{height:157px}
.page-title{position:absolute;color:var(--white);font-weight:500;font-size:14px}
.card{position:absolute;background:var(--white);box-shadow:0 1px 3px rgba(0,0,0,.18)}
.grid-head,.grid-row{display:grid;align-items:center;font-size:10px}
.grid-head{font-weight:500;height:44px;border-bottom:1px solid var(--line)}
.grid-row{height:33.3px;color:var(--ink)}
.grid-row:nth-child(even){background:var(--stripe)}
.pager{height:39px;display:flex;align-items:center;padding-left:29px;font-size:8px;color:var(--ink-soft)}
.pager .sel{margin-left:24px;display:flex;align-items:center;gap:4px}
.pager .range{margin-left:24px}
.pager .nav{margin-left:26px;display:flex;gap:30px}
/* list screen */
.search-field{position:absolute;left:50px;top:105px;width:220px;height:26px;background:rgba(255,255,255,.08);font-size:8.5px;color:#cfd8e6;padding:8px 9px}
.filters{position:absolute;left:650px;top:113px;font-size:8.5px;color:#cfd8e6}
.status{position:absolute;left:678px;top:105px;width:166px;height:26px;background:rgba(255,255,255,.08);font-size:8.5px;color:#cfd8e6;padding:8px 30px 0 0;text-align:right}
.list-grid{grid-template-columns:27px 151px 174px 125px 125px 167px 1fr}
.fab{position:absolute;left:834px;top:483px;width:38px;height:38px;border-radius:50%;background:var(--navy);box-shadow:0 2px 5px rgba(0,0,0,.3);display:flex;align-items:center;justify-content:center;color:#fff;font-size:20px}
.scrim{position:absolute;inset:0;background:var(--scrim);z-index:5}
.dialog{position:absolute;left:275px;top:101px;width:336px;height:354px;background:var(--white);z-index:6;box-shadow:0 4px 14px rgba(0,0,0,.35)}
.dialog-title{height:60px;border-bottom:1px solid #d6d6d6;display:flex;align-items:center;justify-content:center;color:var(--gold);font-weight:500;font-size:13.5px}
.field{position:absolute;left:29px;width:278px;height:24px;border-bottom:1px solid #d0d0d0;font-size:9px;color:#555;padding-left:2px}
.field--active{border-bottom-color:var(--gold)}
.btn-continue{position:absolute;left:233px;top:305px;width:78px;height:25px;background:var(--gold);color:var(--white);font-weight:500;font-size:9.5px;display:flex;align-items:center;justify-content:center;box-shadow:0 1px 3px rgba(0,0,0,.3)}
/* quote screen */
.customer-select{position:absolute;left:566px;top:62px;width:166px;height:28px;background:var(--navy-field);color:var(--white);font-size:9.5px;font-weight:500;display:flex;align-items:center}
.customer-select .name{flex:1;text-align:center;padding-left:28px}
.customer-select .arrows{width:28px;height:100%;border-left:1px solid rgba(255,255,255,.5);display:flex;align-items:center;justify-content:center}
.staff-toggle{position:absolute;left:766px;top:68px;display:flex;align-items:center;color:var(--white);font-size:9.5px;font-weight:500}
.switch{position:relative;margin-left:14px;width:38px;height:14px}
.switch .track{position:absolute;left:4px;top:6px;width:32px;height:2px;background:#6b82aa}
.switch .knob{position:absolute;left:0;top:-2px;width:18px;height:18px;border-radius:50%;background:#2a4d8a}
.product-search{position:absolute;left:30px;top:103px;width:827px;height:27px;background:var(--navy-field);display:flex;align-items:center;color:var(--white);font-size:9.5px;font-weight:500}
.product-search .text{flex:1;padding-left:21px}
.product-search .go{width:59px;height:100%;border-left:1px solid rgba(255,255,255,.35);display:flex;align-items:center;justify-content:center}
.quote-grid{grid-template-columns:27px 51px 123px 102px 123px 176px 100px 67px 1fr}
.sorted{position:relative;color:var(--gold);height:100%;display:flex;align-items:center}
.sorted::after{content:"";position:absolute;left:0;bottom:0;width:96px;height:2px;background:var(--gold)}
.trash{width:10px;height:12px;margin-left:16px}
</style>
</head>
<body>

<!-- Quote list with new-customer dialog -->
<section class="screen screen--list">
  <header class="appbar">
    <svg class="menu-icon" viewBox="0 0 13 10"><path d="M0 1h13M0 5h13M0 9h13" stroke="#777" stroke-width="1.3"/></svg>
    <span class="brand">LOGOHERE</span>
    <span class="greeting">Hi !, Admin Name</span>
    <div class="avatar" role="img" aria-label="User profile photo"></div>
    <svg class="more" viewBox="0 0 3 11"><circle cx="1.5" cy="1.5" r="1.3" fill="#777"/><circle cx="1.5" cy="5.5" r="1.3" fill="#777"/><circle cx="1.5" cy="9.5" r="1.3" fill="#777"/></svg>
  </header>
  <div class="band"></div>
  <h1 class="page-title" style="left:49px;top:66px">Pumbling Showroom Quote System</h1>
  <div class="search-field">Search by quote or customer name</div>
  <div class="filters">Filters</div>
  <div class="status">Open</div>
  <div class="card" style="left:29px;top:151px;width:830px;height:390px">
    <div class="grid-head list-grid"><span></span><span>Quote #</span><span>Costumer Name</span><span>Date</span><span>Total</span><span>Description</span><span>Action</span></div>
    <div class="grid-body">
      <div class="grid-row list-grid"><span></span><span>00123456799</span><span>Nolan Price</span><span>2017-09-30</span><span>$ 5,300.00</span><span>New house upgrade</span><span>✎</span></div>
      <div class="grid-row list-grid"><span></span><span>00123456799</span><span>Nolan Price</span><span>2017-09-30</span><span>$ 5,300.00</span><span>New house upgrade</span><span>✎</span></div>
      <div class="grid-row list-grid"><span></span><span>00123456799</span><span>Nolan Price</span><span>2017-09-30</span><span>$ 5,300.00</span><span>New house upgrade</span><span>✎</span></div>
      <div class="grid-row list-grid"><span></span><span>00123456799</span><span>Nolan Price</span><span>2017-09-30</span><span>$ 5,300.00</span><span>New house upgrade</span><span>✎</span></div>
      <div class="grid-row list-grid"><span></span><span>00123456799</span><span>Nolan Price</span><span>2017-09-30</span><span>$ 5,300.00</span><span>New house upgrade</span><span>✎</span></div>
      <div class="grid-row list-grid"><span></span><span>00123456799</span><span>Nolan Price</span><span>2017-09-30</span><span>$ 5,300.00</span><span>New house upgrade</span><span>✎</span></div>
      <div class="grid-row list-grid"><span></span><span>00123456799</span><span>Nolan Price</span><span>2017-09-30</span><span>$ 5,300.00</span><span>New house upgrade</span><span>✎</span></div>
      <div class="grid-row list-grid"><span></span><span>00123456799</span><span>Nolan Price</span><span>2017-09-30</span><span>$ 5,300.00</span><span>New house upgrade</span><span>✎</span></div>
      <div class="grid-row list-grid"><span></span><span>00123456799</span><span>Nolan Price</span><span>2017-09-30</span><span>$ 5,300.00</span><span>New house upgrade</span><span>✎</span></div>
    </div>
    <div class="pager"><span>Rows per page:</span><span class="sel">7 ▾</span><span class="range">1-7 of 13</span><span class="nav"><span>‹</span><span>›</span></span></div>
  </div>
  <div class="fab">+</div>
  <div class="scrim"></div>
  <div class="dialog" role="dialog" aria-label="Customer information">
    <div class="dialog-title">Please fill out the costumer’s information</div>
    <div class="field field--active" style="top:84px">Name</div>
    <div class="field" style="top:126px">Address</div>
    <div class="field" style="top:168px">Phone</div>
    <div class="field" style="top:209px">Cell</div>
    <div class="field" style="top:251px">E-Mail</div>
    <div class="btn-continue">CONTINUE</div>
  </div>
</section>

<!-- Customer quote detail -->
<section class="screen screen--quote">
  <header class="appbar">
    <svg class="menu-icon" viewBox="0 0 13 10"><path d="M0 1h13M0 5h13M0 9h13" stroke="#777" stroke-width="1.3"/></svg>
    <span class="brand">LOGOHERE</span>
    <span class="greeting">Hi !, Admin Name</span>
    <div class="avatar" role="img" aria-label="User profile photo"></div>
    <svg class="more" viewBox="0 0 3 11"><circle cx="1.5" cy="1.5" r="1.3" fill="#777"/><circle cx="1.5" cy="5.5" r="1.3" fill="#777"/><circle cx="1.5" cy="9.5" r="1.3" fill="#777"/></svg>
  </header>
  <div class="band"></div>
  <h1 class="page-title" style="left:49px;top:67px">Costumer View &nbsp;|&nbsp; Quote #1234</h1>
  <div class="customer-select">
    <span class="name">Dana Reeves</span>
    <span class="arrows"><svg width="8" height="11" viewBox="0 0 8 11"><path d="M1 4l3-3 3 3M1 7l3 3 3-3" fill="none" stroke="#fff" stroke-width="1.3"/></svg></span>
  </div>
  <div class="staff-toggle">Staff<span class="switch"><span class="track"></span><span class="knob"></span></span></div>
  <div class="product-search">
    <span class="text">Search by WFS#, product code, manufacturer code or description to find a product</span>
    <span class="go"><svg width="10" height="10" viewBox="0 0 10 10"><circle cx="4" cy="4" r="3" fill="none" stroke="#fff" stroke-width="1.6"/><path d="M6.2 6.2L9 9" stroke="#fff" stroke-width="1.8"/></svg></span>
  </div>
  <div class="card" style="left:29px;top:151px;width:830px;height:390px">
    <div class="grid-head quote-grid">
      <span></span><span>QTY</span>
      <span class="sorted"><svg width="8" height="9" viewBox="0 0 8 9" style="margin-right:7px"><path d="M4 9V1M1 4l3-3 3 3" fill="none" stroke="#b8954a" stroke-width="1.2"/></svg>WFS</span>
      <span>Product Code</span><span>Manufacturer Code</span><span>Description</span><span>Cost</span><span>View</span><span>Remove</span>
    </div>
    <div class="grid-body">
      <div class="grid-row quote-grid"><span></span><span>1</span><span>83MB106-82</span><span>008168961A</span><span>106010500</span><span>Harlow Non-Insulated Tank</span><span>$123.00</span><span>View</span><svg class="trash" viewBox="0 0 10 12"><path d="M0 1.5h10v1.3H0zM3.5 0h3v1.5h-3zM1 3.3h8l-.7 8.7H1.7z" fill="#b8954a"/></svg></div>
      <div class="grid-row quote-grid"><span></span><span>2</span><span>83MB106-82</span><span>008168961A</span><span>106010500</span><span>Harlow Non-Insulated Tank</span><span>$123.00</span><span>View</span><svg class="trash" viewBox="0 0 10 12"><path d="M0 1.5h10v1.3H0zM3.5 0h3v1.5h-3zM1 3.3h8l-.7 8.7H1.7z" fill="#b8954a"/></svg></div>
      <div class="grid-row quote-grid"><span></span><span>1</span><span>83MB106-82</span><span>008168961A</span><span>106010500</span><span>Harlow Non-Insulated Tank</span><span>$123.00</span><span>View</span><svg class="trash" viewBox="0 0 10 12"><path d="M0 1.5h10v1.3H0zM3.5 0h3v1.5h-3zM1 3.3h8l-.7 8.7H1.7z" fill="#b8954a"/></svg></div>
      <div class="grid-row quote-grid"><span></span><span>1</span><span>83MB106-82</span><span>008168961A</span><span>106010500</span><span>Harlow Non-Insulated Tank</span><span>$123.00</span><span>View</span><svg class="trash" viewBox="0 0 10 12"><path d="M0 1.5h10v1.3H0zM3.5 0h3v1.5h-3zM1 3.3h8l-.7 8.7H1.7z" fill="#b8954a"/></svg></div>
      <div class="grid-row quote-grid"><span></span><span>21</span><span>83MB106-82</span><span>008168961A</span><span>106010500</span><span>Harlow Non-Insulated Tank</span><span>$123.00</span><span>View</span><svg class="trash" viewBox="0 0 10 12"><path d="M0 1.5h10v1.3H0zM3.5 0h3v1.5h-3zM1 3.3h8l-.7 8.7H1.7z" fill="#b8954a"/></svg></div>
      <div class="grid-row quote-grid"><span></span><span>1</span><span>83MB106-82</span><span>008168961A</span><span>106010500</span><span>Harlow Non-Insulated Tank</span><span>$123.00</span><span>View</span><svg class="trash" viewBox="0 0 10 12"><path d="M0 1.5h10v1.3H0zM3.5 0h3v1.5h-3zM1 3.3h8l-.7 8.7H1.7z" fill="#b8954a"/></svg></div>
      <div class="grid-row quote-grid"><span></span><span>7</span><span>83MB106-82</span><span>008168961A</span><span>106010500</span><span>Harlow Non-Insulated Tank</span><span>$123.00</span><span>View</span><svg class="trash" viewBox="0 0 10 12"><path d="M0 1.5h10v1.3H0zM3.5 0h3v1.5h-3zM1 3.3h8l-.7 8.7H1.7z" fill="#b8954a"/></svg></div>
      <div class="grid-row quote-grid"><span></span><span>10</span><span>83MB106-82</span><span>008168961A</span><span>106010500</span><span>Harlow Non-Insulated Tank</span><span>$123.00</span><span>View</span><svg class="trash" viewBox="0 0 10 12"><path d="M0 1.5h10v1.3H0zM3.5 0h3v1.5h-3zM1 3.3h8l-.7 8.7H1.7z" fill="#b8954a"/></svg></div>
      <div class="grid-row quote-grid"><span></span><span>1</span><span>83MB106-82</span><span>008168961A</span><span>106010500</span><span>Harlow Non-Insulated Tank</span><span>$123.00</span><span>View</span><svg class="trash" viewBox="0 0 10 12"><path d="M0 1.5h10v1.3H0zM3.5 0h3v1.5h-3zM1 3.3h8l-.7 8.7H1.7z" fill="#b8954a"/></svg></div>
    </div>
    <div class="pager"><span>Rows per page:</span><span class="sel">7 <svg width="9" height="5" viewBox="0 0 9 5"><path d="M0 0h9L4.5 5z" fill="#b8954a"/></svg></span><span class="range">1-7 of 13</span><span class="nav"><span style="color:#bbb">‹</span><span style="color:#b8954a">›</span></span></div>
  </div>
</section>

</body>
</html>
```